依頼詳細
恥を忍んで書きます。主にシステム側を得意とする自分が、デザインも含めた案件を引き受けてしまい、トップページのデザイン案として以下の2つを作成したところ、クオリティ不足を言い渡されてしまいました。ごもっともだと自覚しています。
http://pelmo.jp/up/tarucs-green.jpg
http://pelmo.jp/up/tarucs-blue.jpg

上記のつたないデザイン案で問題ないのはページ内の「要素」だけですので、デザインのブラッシュアップ、または抜本的なリフレッシュをお願いします。ひとまずトップページ画像だけで大丈夫です。

なお、過去にWordPressテンプレートサイトのデザインに企業名を充てただけの以下のデザインは気に入っていただいています。このテイストをまるごと使ってもかまいません。
http://templates.vorlinquest.com/template_number/live_demo.asp?TemplateID=41938
http://pelmo.jp/up/tarucs-template.jpg

できれば9/2(月)いっぱいくらいで先方に提示したいと考えていて、無謀なスケジュールなので、手を上げていただける方の労力ができるだけ無駄にならないようにしたいです。
サイトURL
http://www.tarucs.co.jp/
ページ数
1ページ
希望イメージ
シンプル 複雑
単色 カラフル
暗い 明るい
日常 高級
遊び心 厳粛
未来的 伝統的
女性的 男性的
希望する色
緑ないし青ベースで、黄と赤をアクセントにとの先方の希望です。
納品ファイル
• 高解像度JPG (.jpg)
• イラストレーター形式 (.ai)
補足説明
ここにメアドを書いていいのかわかりませんが、詳細はお気軽にお問い合わせください。
ご質問など承りますし、素材などもお送りいたします。
mあっとpelmo.jp
追記補足です。
トップページのメイン画像は、
よくある複数パターンの切り替え式(時間経過かクリック)の予定です。
とりあえず今回のご提案では「すばらしい自然を未来の子供たちに…」の
メッセージのもので大丈夫ですが、切り替え式となることをご考慮ください。
これから提案をご予定の方々には申し訳ありません。

過去にクライアントに気に入っていただいたWordPressテンプレートのイメージをうまく活かして、きれいにまとめていただいたdorusan72様に決めさせていただきました。テンプレートのイメージに沿わせるべきか、オリジナリティを出すほうがいいかは、わたしも判断に迷うところでしたが、最終的には先方に選んでいただきました。
青バージョンとして色のイメージを参考にさせていただいたmepolt様、そしてWordPress構築を意識してデザインしていただいたranpu様を次点として選ばせていただきました。

短期のスケジュールだった上に途中でほぼ即決の方向で調整させていただきまして、ランサーの皆様にはご迷惑おかけしてしまいました。
初めてのハルモワークスの利用でしたが、こんなに短期間でクオリティの高いご提案がいただけて大変感激しています。もちろん、次に利用させていただくときはこんなスケジュールにならないようにしたいと思います。
ご提案に至らなかった皆様も含めまして、ありがとうございました。

```html
<!DOCTYPE html>
<html lang="ja">
<head>
<meta charset="utf-8">
<title>Tarucs トップページ</title>
<link rel="stylesheet" href="https://fonts.googleapis.com/css2?family=Noto+Sans+JP:wght@400;700&family=Noto+Serif+JP:wght@700&family=Oswald:wght@500&display=swap">
<style>
:root{
  --green-dark:#3f7d12;
  --green:#6fb22c;
  --green-light:#a9d46a;
  --green-pale:#eef6df;
  --yellow:#f3d42a;
  --red:#d8201a;
  --blue:#2d63b8;
  --text:#333;
  --muted:#777;
  --line:#d9e6c5;
  --white:#fff;
}
*{box-sizing:border-box;margin:0;padding:0}
html,body{width:800px;height:1200px;overflow:hidden}
body{font-family:"Noto Sans JP",sans-serif;color:var(--text);background:var(--white);font-size:11px;position:relative}
.topbar{height:22px;background:var(--green-dark);color:var(--white);font-size:9px;line-height:22px;padding-left:12px;white-space:nowrap;overflow:hidden}
.brand-panel{position:absolute;left:0;top:22px;width:280px;height:245px;background:linear-gradient(160deg,#7cc03a,#4d9a1c);color:var(--white)}
.brand-name{font-family:"Noto Sans JP",sans-serif;font-weight:700;color:var(--white);letter-spacing:1px}
.brand{position:absolute;left:24px;top:32px}
.brand .brand-name{font-size:38px;line-height:1}
.brand-tag{position:absolute;left:24px;top:86px;width:230px;font-size:11px;line-height:1.4}
.contact{position:absolute;left:0;top:138px;width:280px;height:76px;background:var(--white);padding:8px 14px}
.contact small{display:block;font-size:9px;color:var(--text);line-height:1.3}
.tel{font-family:"Oswald",sans-serif;color:var(--red);font-size:28px;line-height:1.3;white-space:nowrap}
.mail-btn{position:absolute;left:12px;top:220px;font-size:10px;color:var(--white);display:flex;gap:6px;align-items:center}
.hero{position:absolute;left:280px;top:22px;width:520px;height:205px;background:linear-gradient(120deg,#d8efb0,#8cc84e 45%,#3f86b8)}
.hero-copy{position:absolute;right:20px;top:14px;font-family:"Noto Serif JP",serif;font-size:19px;color:var(--green-dark);background:rgba(255,255,255,.75);padding:2px 8px;white-space:nowrap}
.slogan{position:absolute;left:280px;top:227px;width:520px;height:40px;background:linear-gradient(#fffbe0,#f1f7d8);font-family:"Noto Serif JP",serif;font-size:17px;color:var(--green-dark);line-height:40px;padding-left:40px;white-space:nowrap}
.nav{position:absolute;left:0;top:267px;width:800px;height:24px;background:linear-gradient(#fafdf2,#e3f0c8);border-top:1px solid var(--line);border-bottom:1px solid var(--line);display:flex}
.nav a{flex:1;text-align:center;font-size:11px;line-height:22px;color:var(--text);text-decoration:none;border-right:1px solid var(--line)}
.side{position:absolute;left:0;top:296px;width:268px}
.feature{margin:0 8px 12px;border:1px solid var(--line);padding:6px;display:flex;gap:6px}
.feature .ph{width:110px;height:80px;flex:none;background:linear-gradient(#cfe3f3,#6b8fa8)}
.feature h3{font-size:11px;color:var(--green-dark);margin-bottom:3px}
.feature p{font-size:9px;color:var(--muted);line-height:1.4}
.menu{margin:20px 8px 0;border-top:2px solid var(--green)}
.menu li{list-style:none;border-bottom:1px dotted var(--green-light);font-size:11px;line-height:26px;padding-left:10px}
.menu li span{color:var(--muted);font-size:9px;margin-left:14px}
.side-btn{display:block;margin:14px 8px 0;height:40px;line-height:40px;text-align:center;font-weight:700;font-size:13px;border-radius:4px}
.btn-yellow{background:var(--yellow);color:var(--green-dark)}
.btn-blue{background:var(--blue);color:var(--white);font-size:16px}
.tiles{position:absolute;left:280px;top:296px;width:512px;display:grid;grid-template-columns:repeat(3,1fr);gap:8px}
.tile{height:128px;position:relative;border:1px solid var(--line)}
.tile b{position:absolute;left:6px;top:6px;background:rgba(255,255,255,.85);color:var(--green-dark);font-family:"Noto Serif JP",serif;font-size:13px;padding:1px 6px}
.t1{background:linear-gradient(#9cc5ea,#38619a)}
.t2{background:linear-gradient(#d9ecf8,#9fb8c9)}
.t3{background:linear-gradient(#f6f6f0,#c9c7b8)}
.t4{background:linear-gradient(#a8d6f0,#4a8fc0)}
.t5{background:linear-gradient(#e8d7b6,#9b7c52)}
.t6{background:linear-gradient(#c9dff2,#6d8cad)}
.news{position:absolute;left:280px;top:574px;width:512px}
.news h2{font-size:14px;color:var(--green-dark);border-bottom:2px solid var(--green);padding:0 0 4px 6px}
.news-item{padding:10px 6px;border-bottom:1px dotted var(--green-light);font-size:10px}
.news-item time{color:var(--green-dark);margin-right:14px}
.news-item strong{color:var(--red);font-weight:400}
.news-item p{color:var(--muted);margin-top:4px;line-height:1.5}
.banners{position:absolute;left:280px;top:892px;width:512px;display:flex;gap:8px}
.banner{flex:1;height:48px;display:flex;align-items:center;justify-content:center;font-weight:700;font-size:13px}
.b1{background:linear-gradient(#1d2b52,#3b5d9a);color:var(--white)}
.b2{background:linear-gradient(#e9f5d3,#a9d46a);color:var(--green-dark)}
.b3{background:linear-gradient(#f2f7fb,#bcd3e6);color:var(--blue)}
.footer{position:absolute;left:0;top:960px;width:800px;height:240px;background:linear-gradient(#b9dd6a,#86c23c)}
.fbrand{position:absolute;left:22px;top:22px}
.fbrand .brand-name{font-size:32px;line-height:1}
.fcontact{position:absolute;left:260px;top:16px;background:var(--white);padding:6px 12px;width:300px}
.fcontact small{font-size:9px;display:block}
.fcontact .tel{font-size:24px}
.fmail{position:absolute;left:580px;top:40px;font-size:10px;color:var(--white);display:flex;gap:6px;align-items:center}
.faddr{position:absolute;left:22px;top:80px;font-size:9px;color:var(--white);line-height:1.5}
.flinks{position:absolute;left:22px;top:124px;display:flex;gap:40px;font-size:11px;color:var(--white)}
.flinks ul{list-style:none}
.flinks li{font-size:9px;line-height:1.7}
.flinks h4{font-size:12px;margin-bottom:2px}
</style>
</head>
<body>
<div class="topbar">Tarucsは未来へつなぐ新エネルギー利用を提案する会社です。新エネルギー技術の企画・開発・施工・研修を行います。</div>

<header class="brand-panel">
  <div class="brand"><span class="brand-name">Tarucs</span></div>
  <p class="brand-tag">新エネルギーで未来をつなぐ</p>
  <div class="contact">
    <small>お問い合わせ・ご相談はお気軽に</small>
    <div class="tel">TEL:072-418-5560</div>
  </div>
  <div class="mail-btn">メールはこちらから
    <svg width="18" height="12" viewBox="0 0 18 12"><rect x="0.5" y="0.5" width="17" height="11" fill="#fff" stroke="#3f7d12"/><path d="M1 1l8 6 8-6" fill="none" stroke="#3f7d12"/></svg>
  </div>
</header>

<div class="hero" role="img" aria-label="緑の葉と地球のイメージ写真"><p class="hero-copy">すばらしい自然を未来の子供たちに残すため</p></div>
<p class="slogan">新しいエネルギー社会を私達と一緒に創りませんか</p>

<nav class="nav"><a>トップページ</a><a>会社概要</a><a>コンサルティング事業</a><a>新エネルギー事業</a><a>ものづくり事業</a></nav>

<aside class="side">
  <div class="feature"><div class="ph" role="img" aria-label="屋根の太陽光パネル写真"></div><div><h3>Sorane社製太陽光発電システム</h3><p>高効率パネルで家庭の電気をまかない、売電も可能なシステムです。</p></div></div>
  <div class="feature"><div class="ph" role="img" aria-label="災害用給水装置の写真" style="background:linear-gradient(#eef2f5,#9aa8b4)"></div><div><h3>SV-Helper［災害用浄水システム］</h3><p>非常時に、雨水・河川水を飲料水に変える浄水装置です。</p></div></div>
  <ul class="menu">
    <li>トップページ<span>Top page</span></li>
    <li>会社概要</li>
    <li>コンサルティング事業</li>
    <li>新エネルギー事業</li>
    <li>ものづくり事業</li>
  </ul>
  <a class="side-btn btn-yellow">講演・シンポジウム情報</a>
  <a class="side-btn btn-blue">Tsunagu Book</a>
</aside>

<section class="tiles">
  <div class="tile t1" role="img" aria-label="太陽光パネル写真"><b>光の力</b></div>
  <div class="tile t2" role="img" aria-label="風力発電機写真"><b>風の力</b></div>
  <div class="tile t3" role="img" aria-label="微生物処理設備写真"><b>微生物の力</b></div>
  <div class="tile t4" role="img" aria-label="水の写真"><b>水の力</b></div>
  <div class="tile t5" role="img" aria-label="自転車発電の写真"><b>人の力</b></div>
  <div class="tile t6" role="img" aria-label="注目設備の写真"><b>PICK UP</b></div>
</section>

<section class="news">
  <h2>お知らせ</h2>
  <div class="news-item"><time>2012.01.01</time><strong>ニューストピックス</strong><p>新しいお知らせの本文がここに入ります。詳細は記事をご覧ください。</p></div>
  <div class="news-item"><time>2012.01.01</time><strong>ニューストピックス</strong><p>新しいお知らせの本文がここに入ります。詳細は記事をご覧ください。</p></div>
  <div class="news-item"><time>2012.01.01</time><strong>ニューストピックス</strong><p>新しいお知らせの本文がここに入ります。詳細は記事をご覧ください。</p></div>
  <div class="news-item"><time>2012.01.01</time><strong>ニューストピックス</strong><p>新しいお知らせの本文がここに入ります。詳細は記事をご覧ください。</p></div>
  <div class="news-item"><time>2012.01.01</time><strong>ニューストピックス</strong><p>新しいお知らせの本文がここに入ります。詳細は記事をご覧ください。</p></div>
</section>

<div class="banners">
  <div class="banner b1">LED STREET LIGHT</div>
  <div class="banner b2">SV-Helper</div>
  <div class="banner b3">新エネルギー研修</div>
</div>

<footer class="footer">
  <div class="fbrand"><span class="brand-name">Tarucs</span></div>
  <div class="fcontact"><small>お問い合わせ・ご相談はお気軽に</small><div class="tel">TEL:072-418-5560</div></div>
  <div class="fmail">メールはこちらから
    <svg width="18" height="12" viewBox="0 0 18 12"><rect x="0.5" y="0.5" width="17" height="11" fill="#fff" stroke="#3f7d12"/><path d="M1 1l8 6 8-6" fill="none" stroke="#3f7d12"/></svg>
  </div>
  <p class="faddr">〒594-0031 大阪府和泉市みどり町2-14-5<br>http://www.tarucs.co.jp/</p>
  <div class="flinks">
    <div><h4>トップ</h4><ul><li>講演・シンポジウム</li><li>Tsunagu Book</li></ul></div>
    <div><h4>会社概要</h4><ul><li>代表挨拶</li><li>アクセス</li></ul></div>
    <div><h4>コンサルティング事業</h4><ul><li>省エネ診断</li><li>導入支援</li></ul></div>
    <div><h4>新エネルギー事業</h4><ul><li>光の力</li><li>風の力</li><li>水の力</li></ul></div>
    <div><h4>ものづくり事業</h4><ul><li>LED照明</li><li>浄水装置</li></ul></div>
  </div>
</footer>
</body>
</html>
```